Business card design needed

Family General Practitioner/ Family Physician.
Logo is the logo of the Crestmoor Guild of Family Clinicians Australia
http://kvplm.tarevo.edu.au/PictureGallery/logos/pages/CGFC%20logo_jpg.htm

Reason: Just a bit more time to make changes and the weekend for me to look at things closely and to choose. Thanks, Lumi

Thanks for all the submissions. So many of them are really works of art. Not one of them are not good. The ones that I am eliminating are the ones that I think are not suitable for me personally only, and because if I don't, it makes it very difficult to decide as many of you are also sending me slight variations of a card. I have just decided to choose a second place card too. Can't thank you all enough. Good luck, Lumi. P.S - Working today till 10 pm as the card says :-), so probably won't be able to give a feedback till late Saturday night or Sunday morning here in Sydney, Australia. 

Reason: Just added a second place to the budget and realised that Australia is ahead of the rest of the world in the time zone (only :-) - don't want to offend anyone or start a debate!! ) , so Monday deadline will mean it will be a weekend for the rest of the world. Just wanted to give everyone more time to submit their best, especially since I will be picking a second card too. Can't thank everyone enough for the submissions. P.S - Not keen on photos on the card.

Contact Information for Business Card

Dr. Lumi Harcourt M.B.B.S., F.C.G.F.C
Family General Practitioner
Address, timings, phone and fax number on the back.

Requirements
Must have
• Timings
Mon 7 am - 7 pm
Tues 7 am - 12 pm
Wed 7 am - 10 pm
Thurs 7 am - 12 pm
Fri 7 am - 8 pm
Sat 8 am - 10 pm
Sun - Off

```html
<!DOCTYPE html>
<html lang="en">
<head>
<meta charset="utf-8">
<title>Dr. Lumi Harcourt – Business Card</title>
<link href="https://fonts.googleapis.com/css2?family=Arimo:wght@400;700&family=Marcellus&display=swap" rel="stylesheet">
<style>
  :root {
    --backdrop: #2b2b2b;
    --card-top: #ffffff;
    --card-bottom: #dcdfdd;
    --band: #4c5a53;
    --band-dark: #3f4b45;
    --ink: #1e1e1e;
    --ink-soft: #3a3a3a;
    --band-text: #ffffff;
    --logo-ink: #4a4a4a;
    --logo-mark: #7b8b83;
  }
  * { margin: 0; padding: 0; box-sizing: border-box; }
  html, body { width: 1200px; height: 861px; overflow: hidden; }
  body {
    background: var(--backdrop);
    font-family: "Arimo", Arial, sans-serif;
    position: relative;
  }
  .card {
    position: absolute;
    top: 275px;
    width: 540px;
    height: 310px;
    border-radius: 16px;
    overflow: hidden;
    background: linear-gradient(180deg, var(--card-top) 0%, var(--card-bottom) 100%);
    box-shadow: 0 10px 30px rgba(0,0,0,.45);
  }
  .card--back { left: 40px; }
  .card--front { left: 620px; }

  .card__texture {
    position: absolute; inset: 0;
    background: radial-gradient(ellipse at 50% 70%, rgba(200,205,202,.35), rgba(255,255,255,0) 70%);
  }

  /* back side */
  .hours { position: absolute; left: 42px; top: 16px; color: var(--ink); }
  .hours__title { font-weight: 700; font-size: 17px; line-height: 21px; margin-bottom: 1px; }
  .hours__table { border-collapse: collapse; font-size: 15.5px; }
  .hours__table td { padding: 0; line-height: 19px; }
  .hours__day { width: 100px; }
  .hours__time small { font-size: 11px; }

  .guild-mark {
    position: absolute;
    display: flex; align-items: center; gap: 10px;
    font-family: "Marcellus", Georgia, serif;
    color: var(--logo-ink);
  }
  .guild-mark__square { width: 14px; height: 14px; background: var(--logo-mark); flex: none; }
  .card--back .guild-mark { left: 350px; top: 55px; width: 170px; font-size: 15px; line-height: 19px; }
  .card--front .guild-mark { left: 140px; top: 40px; width: 300px; font-size: 18px; line-height: 22px; }

  .contact-band {
    position: absolute; left: 0; right: 0; top: 186px; height: 114px;
    background: linear-gradient(180deg, var(--band) 0%, var(--band-dark) 100%);
    color: var(--band-text);
    padding: 11px 0 0 0;
  }
  .contact-row { display: flex; font-size: 15.5px; line-height: 20px; margin-bottom: 7px; }
  .contact-row__label { width: 150px; text-align: right; padding-right: 12px; font-weight: 700; font-size: 16px; }

  /* front side */
  .doctor { position: absolute; left: 0; right: 0; top: 160px; text-align: center; color: var(--ink); }
  .doctor__name { font-family: "Marcellus", Georgia, serif; font-size: 41px; line-height: 46px; font-weight: 400; letter-spacing: .5px; }
  .doctor__credentials { font-size: 14px; line-height: 17px; color: var(--ink-soft); letter-spacing: .5px; margin-top: 2px; }

  .title-band {
    position: absolute; left: 0; right: 0; top: 240px; height: 44px;
    background: linear-gradient(180deg, var(--band) 0%, var(--band-dark) 100%);
    color: var(--band-text);
    display: flex; align-items: center; justify-content: center;
    font-weight: 700; font-size: 20px; letter-spacing: .3px;
  }
</style>
</head>
<body>

  <section class="card card--back" aria-label="Business card, back">
    <div class="card__texture" role="img" aria-label="Faint damask rose pattern across the card"></div>

    <div class="hours">
      <h2 class="hours__title">Working Hours</h2>
      <table class="hours__table">
        <tr><td class="hours__day">Monday</td><td class="hours__time">7:00 <small>AM</small> - 7:00 <small>PM</small></td></tr>
        <tr><td class="hours__day">Tuesday</td><td class="hours__time">7:00 <small>AM</small> - 12:00 <small>PM</small></td></tr>
        <tr><td class="hours__day">Wednesday</td><td class="hours__time">7:00 <small>AM</small> - 10:00 <small>PM</small></td></tr>
        <tr><td class="hours__day">Thursday</td><td class="hours__time">7:00 <small>AM</small> - 12:00 <small>PM</small></td></tr>
        <tr><td class="hours__day">Friday</td><td class="hours__time">7:00 <small>AM</small> - 8:00 <small>PM</small></td></tr>
        <tr><td class="hours__day">Saturday</td><td class="hours__time">8:00 <small>AM</small> - 10:00 <small>PM</small></td></tr>
        <tr><td class="hours__day">Sunday</td><td class="hours__time">Off</td></tr>
      </table>
    </div>

    <div class="guild-mark">
      <span class="guild-mark__square"></span>
      <span>Crestmoor Guild of Family Clinicians Australia</span>
    </div>

    <div class="contact-band">
      <div class="contact-row">
        <span class="contact-row__label">Address</span>
        <span>Level 2, Harbourgate Arcade, Wexley Plaza<br>Shopping Centre Wexley Hill, NSW 2199</span>
      </div>
      <div class="contact-row">
        <span class="contact-row__label">Phone</span>
        <span>02 5550 1847</span>
      </div>
      <div class="contact-row">
        <span class="contact-row__label">Fax</span>
        <span>02 5550 1852</span>
      </div>
    </div>
  </section>

  <section class="card card--front" aria-label="Business card, front">
    <div class="card__texture" role="img" aria-label="Faint damask rose pattern across the card"></div>

    <div class="guild-mark">
      <span class="guild-mark__square"></span>
      <span>Crestmoor Guild of Family Clinicians Australia</span>
    </div>

    <div class="doctor">
      <h1 class="doctor__name">Dr. Lumi Harcourt</h1>
      <p class="doctor__credentials">M.B.B.S., F.C.G.F.C</p>
    </div>

    <div class="title-band">Family General Practitioner</div>
  </section>

</body>
</html>
```